The attached file is what i need on the front of the card. No details to be changed.

On the back could i have as a heading:
We buy for cash $$$
Deceased estates house lots
Antiques, vintage furniture, bikes, kitchenware, automobile, toys,
sports memorabilia, books, records, signage,farm equipment and fashion.

House

```html
<!DOCTYPE html>
<html lang="en">
<head>
<meta charset="utf-8">
<title>2718 Relics – Business Card</title>
<link href="https://fonts.googleapis.com/css2?family=Courier+Prime&family=Open+Sans:wght@400;600;700&family=Grand+Hotel&family=Rubik+Distressed&display=swap" rel="stylesheet">
<style>
  :root {
    --page-bg: #ffffff;
    --card-bg: #ffffff;
    --brand-red: #e8202a;
    --text-dark: #1a1a1a;
    --label-grey: #8a8a8a;
    --card-edge: #3a3a3a;
    --white: #ffffff;
  }
  * { margin: 0; padding: 0; box-sizing: border-box; }
  html, body {
    width: 1200px; height: 818px; overflow: hidden;
    background: var(--page-bg);
  }
  .canvas { position: relative; width: 1200px; height: 818px; }

  .side-label {
    position: absolute; left: 27px;
    font-family: "Courier Prime", monospace;
    font-size: 21px; color: var(--label-grey); letter-spacing: 1px;
  }
  .side-label--front { top: 22px; }
  .side-label--back { top: 450px; }

  .card {
    position: absolute; left: 25px; width: 509px; height: 290px;
    background: var(--card-bg); border: 1px solid var(--card-edge);
    overflow: hidden;
    font-family: "Open Sans", sans-serif; color: var(--text-dark);
  }
  .card--front { top: 51px; }
  .card--back { top: 484px; }

  /* Front */
  .front-band {
    position: absolute; left: 0; top: 0; width: 100%; height: 179px;
    background: var(--brand-red);
  }
  .brand-name {
    position: absolute; left: 0; width: 100%; top: 52px;
    text-align: center; font-family: "Open Sans", sans-serif;
    font-weight: 700; font-size: 54px; color: var(--white); line-height: 1;
  }
  .tagline {
    position: absolute; left: 0; width: 100%; top: 146px;
    text-align: center; font-family: "Grand Hotel", cursive;
    font-size: 23px; color: var(--white); letter-spacing: 0.5px;
  }
  .hours { position: absolute; left: 25px; top: 185px; }
  .hours__title { font-size: 15.5px; font-weight: 700; color: var(--brand-red); line-height: 19px; }
  .hours__line { font-size: 14px; line-height: 16px; padding-left: 27px; }
  .contact-left { position: absolute; left: 25px; top: 238px; font-size: 11px; line-height: 14px; }
  .website { position: absolute; right: 25px; top: 184px; font-size: 12px; font-weight: 700; }
  .phones {
    position: absolute; right: 25px; top: 236px; text-align: right;
    font-size: 12.5px; font-weight: 700; line-height: 15px; letter-spacing: 0.4px;
  }

  /* Back */
  .back-band {
    position: absolute; left: 0; top: 0; width: 100%; height: 95px;
    background: var(--brand-red);
  }
  .back-heading {
    position: absolute; left: 0; width: 100%; top: 20px;
    text-align: center; font-family: "Rubik Distressed", sans-serif;
    font-size: 42px; color: var(--white); line-height: 1; letter-spacing: 1px;
  }
  .buy-list {
    position: absolute; top: 106px; list-style: none;
    font-size: 17.5px; font-weight: 600; line-height: 21.7px;
  }
  .buy-list--left { left: 24px; }
  .buy-list--right { left: 278px; }
  .buy-list li { position: relative; padding-left: 16px; }
  .buy-list li::before {
    content: ""; position: absolute; left: 0; top: 10px;
    width: 6px; height: 6px; border-radius: 50%; background: var(--brand-red);
  }
</style>
</head>
<body>
<main class="canvas">
  <p class="side-label side-label--front">Front</p>
  <section class="card card--front" aria-label="Card front">
    <div class="front-band"></div>
    <p class="brand-name">2718 Relics</p>
    <p class="tagline">Vintage - Retro Clothing &amp; Collectables</p>
    <div class="hours">
      <p class="hours__title">OPEN 6 DAYS A WEEK</p>
      <p class="hours__line">10:00am - 5:00pm</p>
      <p class="hours__line">CLOSED TUESDAYS</p>
    </div>
    <div class="contact-left">
      <p>2718 Harbour View Rd. Elmdale 3920</p>
      <p>Email: info@2718relics.com.au</p>
    </div>
    <p class="website">www.2718relics.com.au</p>
    <div class="phones">
      <p>Phone: 59 555 012</p>
      <p>Mobile: 0400 555 287</p>
    </div>
  </section>

  <p class="side-label side-label--back">Back</p>
  <section class="card card--back" aria-label="Card back">
    <div class="back-band"></div>
    <h1 class="back-heading">WE BUY FOR CASH $$$</h1>
    <ul class="buy-list buy-list--left">
      <li>Deceased estates<br>house lots</li>
      <li>Antiques</li>
      <li>Vintage furniture</li>
      <li>Bikes</li>
      <li>Kitchenware</li>
      <li>Automobile</li>
    </ul>
    <ul class="buy-list buy-list--right">
      <li>Toys</li>
      <li>Sports memorabilia</li>
      <li>Books</li>
      <li>Records</li>
      <li>Signage</li>
      <li>Farm equipment and<br>fashion</li>
    </ul>
  </section>
</main>
</body>
</html>
```